Brackenfold Lane Vineyard website

I need to have our website design done. It is an existing site www.brackenfoldlane.com.au which is based on Wordpress which includes information and online purchasing of our wine. Logo and existing branding are to be maintained but website needs to be improved and open to recommendations for function extensions.

Target Market(s)

Wine drinkers and people wanting to visit or hold and event.
Aged from 25-55, men and women

Industry/Entity Type

Vineyard

Number of Pages Required

5+ page

Font styles to use
Sans Serif

Requirements
Must have
• Incorporate existing logos and styling from bottles.
• See existing website www.brackenfoldlane.com.au

```html
<!DOCTYPE html>
<html lang="en">
<head>
<meta charset="utf-8">
<title>Brackenfold Lane Vineyard</title>
<link href="https://fonts.googleapis.com/css2?family=Open+Sans:wght@400;600;700&family=Tinos:wght@400;700&display=swap" rel="stylesheet">
<style>
:root{
  --green:#2f9a35;
  --green-bar:#3da53a;
  --dark:#232323;
  --footer:#2c2c2c;
  --footer-bottom:#1f1f1f;
  --grey-bg:#eeeeee;
  --text:#444;
  --muted:#9a9a9a;
  --white:#fff;
  --gold:#f5d54a;
}
*{box-sizing:border-box;margin:0;padding:0}
html,body{width:746px;height:1200px;overflow:hidden}
body{position:relative;font-family:"Open Sans",sans-serif;color:var(--text);background:var(--white)}
.abs{position:absolute}

/* top bar */
.topbar{left:0;top:0;width:746px;height:21px;background:var(--green-bar);color:var(--white);font-size:8.5px}
.topbar .item{position:absolute;top:5px;display:flex;align-items:center;gap:6px}
.topbar svg{display:block}

/* header */
.brand{left:223px;top:28px;width:300px;text-align:center}
.brand .mark{width:22px;height:22px;border-radius:50%;background:var(--dark);margin:0 auto 8px}
.brand .name{font-family:"Tinos",serif;font-size:15.5px;letter-spacing:1.3px;color:#222}
.cart{left:560px;top:44px;display:flex;align-items:center}
.cart .badge{width:20px;height:20px;border-radius:50%;background:var(--green);color:#fff;font-size:9px;text-align:center;line-height:20px;margin-left:6px}
.cart .label{margin-left:9px;line-height:1.2}
.cart .label b{display:block;font-family:"Tinos",serif;font-weight:400;font-size:10px;color:#111}
.cart .label span{font-size:8px;color:#444}

/* nav */
.nav{left:38px;top:94px;width:671px;height:36px;background:var(--dark)}
.nav a{position:absolute;top:13px;color:#fff;font-size:9px;text-decoration:none;text-transform:uppercase}
.nav a.active{border-bottom:2px solid var(--green);padding-bottom:5px}
.search{position:absolute;left:521px;top:8px;width:140px;height:20px;background:#fff}
.search .btn{position:absolute;right:0;top:0;width:20px;height:20px;background:var(--green);display:flex;align-items:center;justify-content:center}

/* hero */
.hero{left:0;top:130px;width:746px;height:348px;background:linear-gradient(180deg,#1a2a4c 0%,#23365c 35%,#3a3028 70%,#5a3f22 100%)}
.hero-caption{left:205px;top:318px;width:541px;height:74px;background:linear-gradient(90deg,rgba(0,0,0,.5),rgba(0,0,0,.15))}
.hero-title{left:0;top:323px;width:746px;text-align:center;font-family:"Tinos",serif;font-weight:700;font-size:36px;color:#fff}
.hero-sub{left:0;top:364px;width:746px;text-align:center;font-family:"Tinos",serif;font-size:19px;color:#fff;letter-spacing:.4px}
.arrow{top:248px;width:30px;height:59px;background:rgba(0,0,0,.45);display:flex;align-items:center;justify-content:center}

/* content */
.content-bg{left:0;top:478px;width:746px;height:489px;background:var(--grey-bg)}
.welcome{left:41px;top:499px;width:671px;height:109px;background:#fff;border:1px solid #cfcfcf}
.welcome .pic-left{position:absolute;left:16px;top:6px;width:82px;height:96px;background:linear-gradient(90deg,#5a4a3a,#2f2a26,#8a7a5a);border-radius:4px}
.welcome .pic-right{position:absolute;left:548px;top:12px;width:110px;height:88px;background:radial-gradient(circle at 45% 55%,#2a1d2a,#6b7a35 60%,#fff 85%)}
.welcome h1{position:absolute;left:0;top:16px;width:671px;text-align:center;font-family:"Tinos",serif;font-weight:400;font-size:19px;letter-spacing:.5px;color:#222}
.welcome p{position:absolute;left:118px;top:47px;width:410px;text-align:center;font-size:8px;line-height:14px;color:#555}
.section-title{left:0;top:656px;width:746px;text-align:center;font-family:"Tinos",serif;font-weight:400;font-size:22px;letter-spacing:.5px;color:#222}

.card{top:720px;width:185px;height:172px;background:#fff;border:1px solid #d6d6d6;border-radius:3px;overflow:hidden}
.card .bottle{position:absolute;left:18px;top:20px;width:34px;height:142px;border-radius:12px 12px 3px 3px}
.card .ribbon{position:absolute;left:-22px;top:128px;width:110px;height:22px;background:var(--gold);transform:rotate(45deg);transform-origin:center;color:#2a6a2a;font-size:9px;font-weight:700;text-align:center;line-height:22px;letter-spacing:.5px}
.card h3{position:absolute;left:68px;top:20px;font-family:"Tinos",serif;font-weight:400;font-size:13.5px;line-height:16px;color:#222}
.card p{position:absolute;left:68px;top:56px;width:112px;font-size:8.3px;line-height:14px;color:#333}
.card .price{position:absolute;left:72px;top:90px;font-family:"Tinos",serif;font-weight:700;font-size:28px;color:#222}
.card .price small{font-size:14px}
.card .shop{position:absolute;left:75px;top:130px;width:76px;height:24px;background:var(--green);color:#fff;font-size:10.5px;text-align:center;line-height:24px;border-radius:2px}

/* footer */
.footer{left:0;top:967px;width:746px;height:205px;background:var(--footer);color:var(--muted)}
.footer h4{position:absolute;top:24px;color:#fff;font-size:9px;font-weight:700;text-transform:uppercase}
.f-brand{position:absolute;left:36px;top:22px;width:150px;text-align:center}
.f-brand .mark{width:18px;height:18px;border-radius:50%;background:#fff;margin:0 auto 8px}
.f-brand .name{font-family:"Tinos",serif;font-size:12.5px;letter-spacing:1px;color:#fff}
.f-about{position:absolute;left:36px;top:90px;width:160px;font-size:7.5px;line-height:14px}
.socials{position:absolute;left:37px;top:148px;display:flex;gap:7px}
.socials span{width:19px;height:19px;border-radius:50%;background:#555}
.contact-list{position:absolute;left:209px;top:56px;list-style:none;font-size:7px;color:#bbb}
.contact-list li{display:flex;gap:7px;margin-bottom:9px;line-height:14px}
.contact-list svg{flex:none;margin-top:3px}
.info-list{position:absolute;left:381px;top:59px;list-style:none;font-size:7.5px;color:#aaa}
.info-list li{margin-bottom:11.5px}
.info-list li::before{content:"›";color:var(--green);margin-right:9px}
.news-text{position:absolute;left:553px;top:56px;width:156px;font-size:8px;line-height:17px}
.news-input{position:absolute;left:553px;top:110px;width:156px;height:29px;border:1px solid #666;color:#ddd;font-size:8px;padding:9px 12px}
.news-btn{position:absolute;left:553px;top:151px;width:156px;height:27px;background:var(--green);color:#fff;font-size:8.5px;font-weight:600;text-align:center;line-height:27px}
.copyright{left:0;top:1172px;width:746px;height:28px;background:var(--footer-bottom);color:#8a8a8a;font-size:8px;text-align:center;line-height:28px;letter-spacing:.2px}
</style>
</head>
<body>

<div class="abs topbar">
  <div class="item" style="left:38px">
    <svg width="11" height="10" viewBox="0 0 11 10"><path d="M0 5 L11 1 L7 9 L5.5 6 Z" fill="#fff"/></svg>
    18 Brackenfold Lane · Tarrawong · NSW · 2630 · Australia
  </div>
  <div class="item" style="left:446px">
    <svg width="12" height="9" viewBox="0 0 12 9"><rect x=".5" y=".5" width="11" height="8" fill="none" stroke="#fff"/><path d="M.5 .5 L6 5 L11.5 .5" fill="none" stroke="#fff"/></svg>
    wine@brackenfoldlane.com.au
  </div>
  <div class="item" style="left:604px">
    <svg width="10" height="10" viewBox="0 0 10 10"><path d="M2 0 L4 3 L3 4 Q4.5 6.5 6 7 L7 6 L10 8 L8.5 10 Q2 9 0 1.5 Z" fill="#fff"/></svg>
    +61 400 000 123
  </div>
</div>

<div class="abs brand">
  <div class="mark"></div>
  <div class="name">BRACKENFOLD LANE</div>
</div>

<div class="abs cart">
  <svg width="18" height="16" viewBox="0 0 18 16"><path d="M0 1 H3 L5 10 H15 L17 3 H4" fill="none" stroke="#111" stroke-width="2"/><circle cx="6" cy="14" r="1.6" fill="#111"/><circle cx="14" cy="14" r="1.6" fill="#111"/></svg>
  <div class="badge">0</div>
  <div class="label"><b>SHOPPING CART</b><span>0 item(s) - $0.00 ⌄</span></div>
</div>

<nav class="abs nav">
  <a class="active" style="left:20px">Home</a>
  <a style="left:71px">Wine</a>
  <a style="left:118px">Contact Us</a>
  <a style="left:197px">Events</a>
  <a style="left:253px">Gallery</a>
  <a style="left:315px">About Us</a>
  <a style="left:384px">Members</a>
  <a style="left:450px">Outlets</a>
  <div class="search"><div class="btn"><svg width="11" height="11" viewBox="0 0 11 11"><circle cx="4.5" cy="4.5" r="3.5" fill="none" stroke="#fff" stroke-width="1.5"/><path d="M7 7 L10 10" stroke="#fff" stroke-width="1.6"/></svg></div></div>
</nav>

<div class="abs hero" role="img" aria-label="Evening photo of the vineyard restaurant terrace with lights over the lake and wine being poured"></div>
<div class="abs hero-caption"></div>
<div class="abs hero-title">Enjoy with friends</div>
<div class="abs hero-sub">family and the neighbours</div>
<div class="abs arrow" style="left:0"><svg width="12" height="22" viewBox="0 0 12 22"><path d="M11 1 L1 11 L11 21" fill="none" stroke="#fff" stroke-width="1.6"/></svg></div>
<div class="abs arrow" style="left:716px"><svg width="12" height="22" viewBox="0 0 12 22"><path d="M1 1 L11 11 L1 21" fill="none" stroke="#fff" stroke-width="1.6"/></svg></div>

<div class="abs content-bg"></div>
<section class="abs welcome">
  <div class="pic-left" role="img" aria-label="Row of vineyard wine bottles"></div>
  <h1>WELCOME TO BRACKENFOLD LANE</h1>
  <p>You'll find our boutique vineyard a little way along the road high on the Wattle Ridge Escarpment. Everything is lovingly handpicked and made locally to produce high quality wine, that the Tarrawong District is fast becoming renowned for producing.</p>
  <div class="pic-right" role="img" aria-label="Glass of red wine with a bunch of grapes and vine leaves"></div>
</section>

<h2 class="abs section-title">FEATURED WINE</h2>

<article class="abs card" style="left:56px">
  <div class="bottle" role="img" aria-label="White wine bottle" style="background:linear-gradient(180deg,#cfd6dc 0 20%,#f0ee6a 20%,#d8d83a 100%)"></div>
  <div class="ribbon">BEST CHOICE</div>
  <h3>Sauvignon<br>Blanc 2015</h3>
  <p>consectetur adipiscing elit etiam accumsan</p>
  <div class="price"><small>$</small>18.18</div>
  <div class="shop">Shop Now!</div>
</article>
<article class="abs card" style="left:277px">
  <div class="bottle" role="img" aria-label="Red wine bottle" style="background:linear-gradient(180deg,#6a1420 0 20%,#1e1a1c 20%,#2c2628 100%)"></div>
  <div class="ribbon">BEST CHOICE</div>
  <h3>Sauvignon<br>Blanc 2015</h3>
  <p>consectetur adipiscing elit etiam accumsan</p>
  <div class="price"><small>$</small>18.18</div>
  <div class="shop">Shop Now!</div>
</article>
<article class="abs card" style="left:501px">
  <div class="bottle" role="img" aria-label="Green wine bottle with orange capsule" style="background:linear-gradient(180deg,#f08a1c 0 20%,#3d4a1a 20%,#5a6a22 100%)"></div>
  <div class="ribbon">BEST CHOICE</div>
  <h3>Sauvignon<br>Blanc 2015</h3>
  <p>consectetur adipiscing elit etiam accumsan</p>
  <div class="price"><small>$</small>18.18</div>
  <div class="shop">Shop Now!</div>
</article>

<footer class="abs footer">
  <div class="f-brand"><div class="mark"></div><div class="name">BRACKENFOLD LANE</div></div>
  <p class="f-about">BLV is a registered grower and member of the Tarrawong Valley Growers Association.</p>
  <div class="socials"><span></span><span></span><span></span><span></span></div>

  <h4 style="left:209px">Get in touch</h4>
  <ul class="contact-list">
    <li><svg width="7" height="9" viewBox="0 0 7 9"><path d="M3.5 9 L0.6 4.5 A3.3 3.3 0 1 1 6.4 4.5 Z" fill="#2f9a35"/></svg><span>250 Vine Street, Hollowbrook CA 90000<br>United States</span></li>
    <li><svg width="8" height="8" viewBox="0 0 10 10"><path d="M2 0 L4 3 L3 4 Q4.5 6.5 6 7 L7 6 L10 8 L8.5 10 Q2 9 0 1.5 Z" fill="#2f9a35"/></svg><span>(123) 45600000</span></li>
    <li><svg width="8" height="8" viewBox="0 0 11 10"><path d="M0 5 L11 1 L7 9 L5.5 6 Z" fill="#2f9a35"/></svg><span>info@brackenfoldlane.com.au</span></li>
    <li><svg width="6" height="9" viewBox="0 0 6 9"><rect x=".5" y=".5" width="5" height="8" rx="1" fill="none" stroke="#2f9a35"/></svg><span>(123) 45600000</span></li>
    <li><svg width="8" height="8" viewBox="0 0 8 8"><circle cx="4" cy="4" r="3.4" fill="none" stroke="#2f9a35"/><path d="M4 2 V4 H5.6" fill="none" stroke="#2f9a35"/></svg><span>Mon - Sat: 9:00 - 18:00</span></li>
  </ul>

  <h4 style="left:381px">Information</h4>
  <ul class="info-list">
    <li>WINE</li><li>EVENTS</li><li>GALLERY</li><li>ABOUT US</li><li>MEMBERS</li><li>OUTLETS</li>
  </ul>

  <h4 style="left:553px">News letter</h4>
  <p class="news-text">Enter your email address for our mailing list to keep your self our lastest updated.</p>
  <div class="news-input">Email</div>
  <div class="news-btn">Sign up</div>
</footer>
<div class="abs copyright">COPYRIGHT © 2007 - 2016 BRACKENFOLD LANE.&nbsp; ALL RIGHTS RESERVED</div>

</body>
</html>
```